Personal Blog

The wordpress blog style and layout should be similar to http://www.ninalofwent.com

homepage: my photo, list of things, call to action then 3 boxes (The Blog, The Book and podcast)

Other pages: About us, Blog, Consulting, Contact

Target Market(s)

Web Marketing Consultant

Industry/Entity Type

Consulting

Colors
3277b5
33a6d7
f04a50
f68e4e
33b7a4

```html
<!DOCTYPE html>
<html lang="en">
<head>
<meta charset="utf-8">
<title>Samir Halvorsen – Personal Blog</title>
<link rel="stylesheet" href="https://fonts.googleapis.com/css2?family=Arimo:ital,wght@0,400;0,700;1,400;1,700&family=Roboto+Condensed:wght@400;700&family=Raleway:wght@400;500;600;700&display=swap">
<style>
:root{
  --orange:#d5611b;
  --orange-light:#ec7a2d;
  --ink:#1c1c1c;
  --grey-text:#555;
  --card-bg:#efefef;
  --footer-bg:#232323;
  --footer-bar:#1a1a1a;
  --footer-text:#8a8a8a;
  --white:#fff;
  --line:#d8d8d8;
}
*{box-sizing:border-box;margin:0;padding:0}
html,body{width:793px;height:1200px;overflow:hidden;background:var(--white)}
body{position:relative;font-family:"Arimo",Arial,sans-serif;color:var(--ink)}
.abs{position:absolute}

/* header */
.site-header{position:absolute;left:0;top:0;width:793px;height:67px;background:var(--white);border-bottom:2px solid #e4e4e4}
.brand{position:absolute;left:67px;top:16px;display:flex;align-items:center;gap:8px;height:33px}
.brand-mark{width:22px;height:22px;background:var(--orange-light);border-radius:3px}
.brand-name{font-family:"Raleway",sans-serif;font-weight:700;font-size:21px;color:var(--ink)}
.main-nav{position:absolute;left:340px;top:24px;display:flex;height:22px;font-family:"Roboto Condensed",sans-serif;font-size:12.5px;text-transform:uppercase}
.main-nav a{display:block;padding:0 12px;line-height:22px;color:#222;text-decoration:none;border-left:1px solid #e0e0e0}
.main-nav a:first-child{border-left:none}
.main-nav a.current{color:var(--orange)}

/* hero */
.hero-backdrop{position:absolute;left:0;top:69px;width:793px;height:219px;background:linear-gradient(90deg,#b9b9b9 0%,#dcdcdc 35%,#cfcfcf 65%,#e8e8e8 100%)}
.hero-quote-area{position:absolute;left:0;top:288px;width:793px;height:97px;background:linear-gradient(#fff,#ececec)}
.hero-portrait{position:absolute;left:400px;top:92px;width:297px;height:241px;background:linear-gradient(160deg,#cfcfcf 0%,#9aa0a6 45%,#eeeeee 100%);border-radius:4px}
.hero-title{position:absolute;left:72px;top:90px;font-size:26px;line-height:28px;font-weight:400;color:#111;letter-spacing:-.3px}
.hero-title strong{color:var(--orange);font-weight:700}
.hero-sub{position:absolute;left:72px;top:150px;font-size:17.5px;color:#111}
.topic-list{position:absolute;left:73px;top:181px;list-style:none;font-size:10.5px}
.topic-list li{display:flex;align-items:center;gap:9px;height:21px}
.tick{width:10px;height:10px}
.testimonial{position:absolute;left:75px;top:300px;width:312px}
.testimonial .quote-mark{position:absolute;font-family:Georgia,serif;font-size:40px;color:#bbb;line-height:1}
.testimonial p{position:absolute;left:31px;top:10px;width:283px;font-size:9.8px;font-style:italic;line-height:14.6px;color:#333}
.testimonial p b{color:var(--orange)}
.testimonial cite{position:absolute;right:-2px;top:63px;font-size:7.5px;font-weight:700;font-style:italic;color:#111}

/* feature band */
.feature-band{position:absolute;left:0;top:385px;width:793px;height:280px;background:var(--orange)}
.feature{position:absolute;top:34px;width:200px;text-align:center;color:var(--white)}
.feature-icon{width:86px;height:86px;margin:0 auto;border-radius:50%;background:#f5f5f5;border:2px solid #111;display:flex;align-items:center;justify-content:center}
.feature h2{font-family:"Arimo",sans-serif;font-weight:700;font-size:20px;margin-top:30px;letter-spacing:.3px}
.feature p{font-size:9.3px;line-height:13.5px;margin:6px auto 0;width:170px}
.btn-outline{display:inline-block;margin-top:14px;width:80px;height:26px;line-height:23px;border:1.5px solid var(--white);border-radius:3px;font-size:11px;color:var(--white);text-decoration:none}

/* recent blogs */
.section-title{position:absolute;left:0;top:692px;width:793px;text-align:center;font-family:"Raleway",sans-serif;font-size:18px;font-weight:500;letter-spacing:.8px}
.section-title::before,.section-title::after{content:"";position:absolute;top:11px;width:225px;height:1px;background:var(--line)}
.section-title::before{left:95px}.section-title::after{right:100px}
.post-card{position:absolute;top:747px;width:185px;height:239px;background:var(--card-bg)}
.post-thumb{width:185px;height:128px}
.post-card h3{font-family:"Roboto Condensed",sans-serif;font-size:11px;font-weight:700;line-height:14.5px;margin:8px 9px 0}
.post-card p{font-family:"Roboto Condensed",sans-serif;font-size:8.6px;line-height:11.8px;color:var(--grey-text);margin:4px 9px 0}
.btn-solid{display:inline-block;margin:7px 9px 0;padding:0 6px;height:18px;line-height:18px;background:var(--orange);color:var(--white);font-family:"Roboto Condensed",sans-serif;font-size:8.6px;text-decoration:none}

/* footer */
.site-footer{position:absolute;left:0;top:1013px;width:793px;height:157px;background:var(--footer-bg)}
.footer-col{position:absolute;top:23px}
.footer-col h4{font-family:"Raleway",sans-serif;font-size:11px;font-weight:600;color:var(--white)}
.footer-col p{font-family:"Raleway",sans-serif;font-size:8.6px;line-height:12.4px;color:var(--footer-text)}
.signup input{display:block;width:152px;height:20px;border:none;background:var(--white);font-size:8px;padding-left:5px;font-family:"Arimo",sans-serif;color:#222}
.signup button{display:block;width:152px;height:22px;border:none;background:var(--orange-light);color:var(--white);font-family:"Raleway",sans-serif;font-weight:600;font-size:13px}
.contact-row{position:absolute;left:0;display:flex;gap:10px;font-family:"Raleway",sans-serif;font-size:9.5px;line-height:15px;color:var(--footer-text);width:210px;border-bottom:1px solid #333;padding-bottom:6px}
.contact-row .icon{width:12px;height:12px;margin-top:2px;flex:none}
.contact-row a{color:#e6552b;text-decoration:none}
.footer-bar{position:absolute;left:0;top:1170px;width:793px;height:30px;background:var(--footer-bar);text-align:center;line-height:30px;font-family:"Raleway",sans-serif;font-size:8.8px;color:#999}
</style>
</head>
<body>

<header class="site-header">
  <div class="brand"><span class="brand-mark"></span><span class="brand-name">Samir Halvorsen</span></div>
  <nav class="main-nav">
    <a class="current" href="#">About</a><a href="#">Blog</a><a href="#">Consulting</a><a href="#">Resources</a><a href="#">Book</a><a href="#">Contact</a>
  </nav>
</header>

<section class="hero">
  <div class="hero-backdrop" role="img" aria-label="Blurred bright office meeting room"></div>
  <div class="hero-quote-area"></div>
  <div class="hero-portrait" role="img" aria-label="Portrait of the consultant seated at a desk with a laptop"></div>
  <h1 class="hero-title">Text ho here &amp; <strong>Product<br>Management</strong> text here Online</h1>
  <p class="hero-sub">Marketing, to learn topics:</p>
  <ul class="topic-list">
    <li><svg class="tick" viewBox="0 0 10 10"><circle cx="5" cy="5" r="5" fill="#ec7a2d"/><path d="M2.8 5.2l1.5 1.5 3-3.2" stroke="#fff" stroke-width="1.3" fill="none"/></svg>Product Management</li>
    <li><svg class="tick" viewBox="0 0 10 10"><circle cx="5" cy="5" r="5" fill="#ec7a2d"/><path d="M2.8 5.2l1.5 1.5 3-3.2" stroke="#fff" stroke-width="1.3" fill="none"/></svg>Customer Development</li>
    <li><svg class="tick" viewBox="0 0 10 10"><circle cx="5" cy="5" r="5" fill="#ec7a2d"/><path d="M2.8 5.2l1.5 1.5 3-3.2" stroke="#fff" stroke-width="1.3" fill="none"/></svg>Digital Marketing</li>
    <li><svg class="tick" viewBox="0 0 10 10"><circle cx="5" cy="5" r="5" fill="#ec7a2d"/><path d="M2.8 5.2l1.5 1.5 3-3.2" stroke="#fff" stroke-width="1.3" fill="none"/></svg>Branding &amp; Reputation</li>
  </ul>
  <blockquote class="testimonial">
    <span class="quote-mark" style="left:0;top:0">&ldquo;</span>
    <p>&ldquo;....<b>I was blown away by his</b> breadth of industry knowledge, the straight talking delivery and collaborative format. A highly recommended Social media experts and thought leader...&rdquo;</p>
    <span class="quote-mark" style="left:260px;top:38px">&rdquo;</span>
    <cite>-Owen Marlow - Marketing</cite>
  </blockquote>
</section>

<section class="feature-band">
  <div class="feature" style="left:77px">
    <div class="feature-icon"><svg width="44" height="36" viewBox="0 0 44 36"><path d="M4 13h8l16-9v28l-16-9H4z" fill="#111"/><path d="M9 23l3 10h5l-3-10z" fill="#111"/><path d="M32 11q4 7 0 14M36 8q6 10 0 20" stroke="#111" stroke-width="2" fill="none"/></svg></div>
    <h2>THE BLOG</h2>
    <p>simply dummy text of the printing and typesetting industry. Lorem Ipsum has been the industry's standard dummy text ever</p>
    <a class="btn-outline" href="#">Read More</a>
  </div>
  <div class="feature" style="left:300px">
    <div class="feature-icon"><svg width="48" height="34" viewBox="0 0 48 34"><path d="M24 6Q14 0 3 3v26q11-3 21 3 10-6 21-3V3Q34 0 24 6z" fill="none" stroke="#111" stroke-width="3.5" stroke-linejoin="round"/><path d="M24 6v26" stroke="#111" stroke-width="3"/></svg></div>
    <h2>THE BOOK</h2>
    <p>simply dummy text of the printing and typesetting industry. Lorem Ipsum has been the industry's standard dummy text ever</p>
    <a class="btn-outline" href="#">Read More</a>
  </div>
  <div class="feature" style="left:514px">
    <div class="feature-icon"><svg width="44" height="40" viewBox="0 0 44 40"><circle cx="16" cy="17" r="8" fill="#111"/><path d="M3 38q1-11 13-11t13 11z" fill="#111"/><circle cx="32" cy="10" r="8" fill="#fff" stroke="#111" stroke-width="1.6"/><path d="M32 9v6" stroke="#111" stroke-width="2"/><circle cx="32" cy="6" r="1.2" fill="#111"/></svg></div>
    <h2>CONSULTING</h2>
    <p>simply dummy text of the printing and typesetting industry. Lorem Ipsum has been the industry's standard dummy text ever</p>
    <a class="btn-outline" href="#">Read More</a>
  </div>
</section>

<h2 class="section-title">RECENT BLOGS</h2>

<article class="post-card" style="left:76px">
  <div class="post-thumb" role="img" aria-label="Laptop and coffee cup on a wooden table" style="background:linear-gradient(150deg,#3a2c22,#8a5a35 55%,#c9b9a5)"></div>
  <h3>Yet Another video Post Format With Embedded Media</h3>
  <p>Ipsum is simply dummy text of the printing and typesetting industry. Lorem Ipsum has been the industry's standard</p>
  <a class="btn-solid" href="#">Watch Video</a>
</article>
<article class="post-card" style="left:306px">
  <div class="post-thumb" role="img" aria-label="Desk from above with notebooks, phone and stationery" style="background:linear-gradient(150deg,#c98d64,#e6c4a6 50%,#b8786a)"></div>
  <h3>Yet Another video Post Format With Embedded Media</h3>
  <p>Ipsum is simply dummy text of the printing and typesetting industry. Lorem Ipsum has been the industry's standard</p>
  <a class="btn-solid" href="#">Watch Video</a>
</article>
<article class="post-card" style="left:532px">
  <div class="post-thumb" role="img" aria-label="Person working on a laptop at a cafe table" style="background:linear-gradient(150deg,#1e1c1b,#5a4636 50%,#2f3a48)"></div>
  <h3>Yet Another video Post Format With Embedded Media</h3>
  <p>Ipsum is simply dummy text of the printing and typesetting industry. Lorem Ipsum has been the industry's standard</p>
  <a class="btn-solid" href="#">Watch Video</a>
</article>

<footer class="site-footer">
  <div class="footer-col" style="left:90px;width:185px">
    <h4>About IT Consultants</h4>
    <p style="margin-top:11px">Lorem Ipsum is simply dummy text of the printing and typesetting industry. Lorem Ipsum has been the industry's standard dummy text ever since the 1500s, when an unknown printer took a galley of type and scrambled it to make a type specimen book. It has survived not only five centuries.</p>
  </div>
  <div class="footer-col signup" style="left:302px">
    <h4>Join My New Business</h4>
    <input style="margin-top:12px" type="text" placeholder="Enter Your Name">
    <input style="margin-top:12px" type="email" placeholder="Enter Email Name">
    <button style="margin-top:9px" type="button">Join For Free!</button>
  </div>
  <div class="footer-col" style="left:521px;width:220px;height:140px">
    <h4>Contact Us</h4>
    <div class="contact-row" style="top:19px">
      <svg class="icon" viewBox="0 0 12 12"><path d="M1 2h10v2H7v7H5V4H1z" fill="#777"/></svg>
      <span>Harbor Lane Studio<br>1180 Alder Grove Rd, Suite 210<br>Millbrook, OR 97000</span>
    </div>
    <div class="contact-row" style="top:84px">
      <svg class="icon" viewBox="0 0 12 12"><path d="M2 1l3 1-1 3q1 2 3 3l3-1 1 3-2 1Q3 10 1 3z" fill="#777"/></svg>
      <span>+(00) 555 010 2040</span>
    </div>
    <div class="contact-row" style="top:113px">
      <svg class="icon" viewBox="0 0 12 12"><rect x="1" y="3" width="10" height="7" fill="#777"/><path d="M1 3l5 4 5-4" stroke="#232323" fill="none"/></svg>
      <a href="#">hello@harborlane.example</a>
    </div>
  </div>
</footer>
<div class="footer-bar">© 2014 Copyright - Samir Halvorsen . All rights reserved</div>

</body>
</html>
```